Sports Nutrition Package Labels

Need a design for a label for a pre-workout supplement. The design would need to include:
* The company colors of a neon and dark neon green. (logo attached)
* The concept would need to incorporate the idea of hacking, futuristic, technology, digital, molecular biology and supplements for an ultra modern eye catching and streamline looking label. (Quorvex)
* Name of the company "Quorvex Supplements" will need to be included by the logo.
* Need label with size to match the attached template below. Along with bottle mock up to be used for online store. (Bottles will be black)
* Google image "Cyber Punk" or "Bio Punk" for an idea of the culture behind Quorvex.

Inspiration:
http://snapvault.example/4472913/
http://lumotiles.example/cyberpunk_by_nightquillion-wallpapers.html
http://www.backdropz88.example/thumbnails/detail/20120229/green%20abstract%20black%201920x1200%20wallpaper_www.backdropz88.example_27.jpg

**** If details of ask are to vague, feel free to reach out to me ****

Project will start out with one product and if works out it will expand to requesting designs for brochures and other products - looking for a long lasting and on-going business relationship.
Attached is a copy of a basic template that includes the wording for the label as well as two photos of competitions products that I like the designs of.

I'm leaving a lot of this up to your good judgement and creativity.

Target Market(s)

Male and Female interested in fitness between ages 18 to 50

Industry/Entity Type

Business

Requirements
Must have
• Mix of Molecular Biology and Technology - such as "Quorvex" Taking a hackers approach to vitamins.
Nice to have
• Molecules, Neon Green and Dark Neon green as majority along with black background.
Should not have
• Old looking designs.

```html
<!DOCTYPE html>
<html lang="en">
<head>
<meta charset="utf-8">
<title>Pre Quorvex – Pre-Workout Label</title>
<link rel="stylesheet" href="https://fonts.googleapis.com/css2?family=Arimo:wght@400;700&family=Roboto+Condensed:wght@700&display=swap">
<style>
  :root {
    --page-bg: #d9d9d9;
    --label-deep: #06150d;
    --label-mid: #0f3d24;
    --label-glow: #1d5c37;
    --neon: #35e07a;
    --neon-dark: #0f8a44;
    --text-white: #ffffff;
    --text-yellow: #f3e520;
    --badge-orange: #f39a1e;
    --badge-red: #d8202a;
    --badge-ink: #222222;
  }
  * { margin: 0; padding: 0; box-sizing: border-box; }
  html, body { width: 782px; height: 1200px; overflow: hidden; }
  body {
    background: var(--page-bg);
    font-family: "Arimo", Arial, sans-serif;
    position: relative;
  }
  .label {
    position: absolute;
    left: 41px;
    top: 385px;
    width: 700px;
    height: 430px;
    background:
      radial-gradient(ellipse 60% 55% at 45% 40%, var(--label-glow) 0%, transparent 70%),
      linear-gradient(180deg, var(--label-mid) 0%, var(--label-deep) 100%);
    color: var(--text-white);
    overflow: hidden;
  }
  .brand-mark {
    position: absolute;
    left: 293px;
    top: 18px;
    display: flex;
    align-items: center;
    gap: 6px;
  }
  .brand-mark .dot {
    width: 14px; height: 14px; border-radius: 50%;
    background: var(--neon);
  }
  .brand-mark .company {
    font-size: 13px; font-weight: 700; color: var(--neon);
    letter-spacing: 0.5px;
  }
  .product-prefix {
    position: absolute; left: 196px; top: 56px;
    font-size: 38px; font-weight: 700;
  }
  .product-name {
    position: absolute; left: 188px; top: 90px;
    font-size: 88px; font-weight: 700; letter-spacing: -1px;
    line-height: 1;
  }
  .benefits {
    position: absolute; left: 150px; top: 200px;
    font-family: "Roboto Condensed", "Arial Narrow", sans-serif;
    font-size: 24px; font-weight: 700; color: var(--text-yellow);
    letter-spacing: 1px; word-spacing: 4px;
  }
  .tagline {
    position: absolute; left: 176px; top: 236px;
    font-size: 27px; font-weight: 700;
  }
  .energy-art {
    position: absolute; left: 150px; top: 275px;
    width: 330px; height: 110px;
    background: radial-gradient(ellipse 50% 60% at 55% 40%, rgba(120,255,180,0.55) 0%, rgba(30,160,90,0.35) 40%, transparent 75%);
  }
  .flavor-badge {
    position: absolute; left: 548px; top: 236px;
    width: 116px; height: 116px;
  }
  .net-weight {
    position: absolute; left: 158px; top: 370px;
    font-size: 30px;
  }
  .net-weight small { font-size: 19px; }
  .servings {
    position: absolute; left: 470px; top: 360px;
    text-align: left;
  }
  .servings .count {
    font-size: 28px; font-weight: 700; color: var(--text-yellow);
  }
  .servings .kind { font-size: 18px; }
</style>
</head>
<body>
  <section class="label">
    <div class="brand-mark"><span class="dot"></span><span class="company">Quorvex Supplements</span></div>
    <div class="product-prefix">Pre</div>
    <h1 class="product-name">Quorvex</h1>
    <p class="benefits">STRENTH POWER ENDURANCE FOCUS</p>
    <p class="tagline">Be Biologically Diffetent</p>
    <div class="energy-art" role="img" aria-label="Glowing neon green abstract energy swirls"></div>

    <svg class="flavor-badge" viewBox="0 0 120 120" role="img" aria-label="Fruit punch natural flavors">
      <defs>
        <path id="badge-top-arc" d="M 28 60 A 32 32 0 0 1 92 60"/>
        <path id="badge-bottom-arc" d="M 24 60 A 36 36 0 0 0 96 60"/>
      </defs>
      <polygon fill="var(--badge-orange)" points="60,2 67,14 80,6 83,20 98,17 96,31 110,33 103,46 116,54 105,63 114,75 100,79 104,93 90,93 89,107 76,102 70,115 60,106 50,115 44,102 31,107 30,93 16,93 20,79 6,75 15,63 4,54 17,46 10,33 24,31 22,17 37,20 40,6 53,14"/>
      <circle cx="60" cy="60" r="42" fill="#ffffff"/>
      <text font-family="Arimo, Arial, sans-serif" font-size="10" font-weight="700" fill="var(--badge-ink)">
        <textPath href="#badge-top-arc" startOffset="50%" text-anchor="middle">FRUIT PUNCH</textPath>
      </text>
      <circle cx="60" cy="62" r="12" fill="var(--badge-red)"/>
      <text font-family="Arimo, Arial, sans-serif" font-size="7.5" font-weight="700" fill="var(--badge-orange)">
        <textPath href="#badge-bottom-arc" startOffset="50%" text-anchor="middle" dominant-baseline="hanging">NATURAL FLAVORS</textPath>
      </text>
    </svg>

    <div class="net-weight">315 G <small>(0.69 LB)</small></div>
    <div class="servings">
      <div class="count">44 SERVINGS</div>
      <div class="kind">Dietary Supplement</div>
    </div>
  </section>
</body>
</html>
```